Business Card Design Project

I need a business card for an environmentally friendly interior design company called Maplecrest Decor.
I was thinking it might be nice to print the business cards on brown recycled paper with green ink.
In addition to interior design, I will also be able to consult with homeowners regarding their indoor environments and how they might be affecting their health after May 2013 which is when I will complete my certification program. This can be added to the business card at that time: "Certified Dwelling Vitality Environmental Consultant".

```html
<!DOCTYPE html>
<html lang="en">
<head>
<meta charset="utf-8">
<title>Maplecrest Decor – Business Card</title>
<link rel="stylesheet" href="https://fonts.googleapis.com/css2?family=Cinzel:wght@400;700&display=swap">
<style>
  :root {
    --ink-green: #0d7a2c;
    --ink-brown: #4a3b0c;
    --paper-white: #ffffff;
    --paper-kraft: #e8d5aa;
    --paper-kraft-light: #efe0bd;
    --frame: #5a4a18;
    --page: #ffffff;
  }
  * { margin: 0; padding: 0; box-sizing: border-box; }
  html, body {
    width: 1200px;
    height: 832px;
    overflow: hidden;
    background: var(--page);
  }
  .canvas {
    position: relative;
    width: 1200px;
    height: 832px;
  }
  .card {
    position: absolute;
    top: 87px;
    width: 447px;
    height: 676px;
    border: 1.5px solid var(--frame);
    font-family: "Cinzel", serif;
  }
  .card--white { left: 53px; background: var(--paper-white); }
  .card--kraft {
    left: 605px;
    background: radial-gradient(circle at 60% 40%, var(--paper-kraft-light), var(--paper-kraft) 70%);
  }
  .brand {
    position: absolute;
    top: 14px;
    left: 20px;
    right: 20px;
  }
  .brand__line1 {
    display: block;
    color: var(--ink-green);
    font-size: 52px;
    line-height: 1;
    letter-spacing: 1px;
  }
  .brand__line2 {
    display: block;
    text-align: right;
    color: var(--ink-brown);
    font-size: 60px;
    line-height: 1.05;
    letter-spacing: 1px;
  }
  .tagline {
    position: absolute;
    top: 164px;
    left: 0;
    right: 0;
    text-align: center;
    color: var(--ink-green);
    font-size: 15px;
    letter-spacing: 0.5px;
  }
  .band {
    position: absolute;
    left: 0;
    right: 0;
    height: 12px;
    background: var(--ink-brown);
  }
  .band--top { top: 195px; }
  .band--bottom { top: 537px; }
  .floral-art {
    position: absolute;
    top: 212px;
    left: 0;
    right: 0;
    height: 320px;
    background: linear-gradient(120deg, #6a5620 0%, #8a7a3a 45%, #2f8a45 100%);
    opacity: 0.85;
  }
  .contact {
    position: absolute;
    top: 560px;
    left: 20px;
    right: 20px;
    display: flex;
    justify-content: space-between;
    color: var(--ink-brown);
    font-size: 21px;
  }
  .credentials {
    position: absolute;
    top: 606px;
    left: 20px;
    right: 10px;
    color: var(--ink-green);
    font-weight: 700;
    font-size: 17px;
    line-height: 1.3;
  }
</style>
</head>
<body>
<main class="canvas">
  <section class="card card--white">
    <h1 class="brand">
      <span class="brand__line1">MAPLECREST</span>
      <span class="brand__line2">DECOR</span>
    </h1>
    <p class="tagline">ENVIRONMENTALLY FRIENDLY DESIGN</p>
    <div class="band band--top"></div>
    <div class="floral-art" role="img" aria-label="Stylised floral illustration of flowers and leaves in green and brown"></div>
    <div class="band band--bottom"></div>
    <p class="contact"><span class="contact__name">Dana Lee Whitfield</span><span class="contact__phone">555·204·7316</span></p>
    <p class="credentials">CERTIFIED DWELLING VITALITY<br>ENVIRONMENTAL CONSULTANT</p>
  </section>

  <section class="card card--kraft">
    <h1 class="brand">
      <span class="brand__line1">MAPLECREST</span>
      <span class="brand__line2">DECOR</span>
    </h1>
    <p class="tagline">ENVIRONMENTALLY FRIENDLY DESIGN</p>
    <div class="band band--top"></div>
    <div class="floral-art" role="img" aria-label="Stylised floral illustration of flowers and leaves in green and brown on kraft paper"></div>
    <div class="band band--bottom"></div>
    <p class="contact"><span class="contact__name">Dana Lee Whitfield</span><span class="contact__phone">555·204·7316</span></p>
    <p class="credentials">CERTIFIED DWELLING VITALITY<br>ENVIRONMENTAL CONSULTANT</p>
  </section>
</main>
</body>
</html>
```